Harbor of Mercy - Team of Rabbis and Doctors Helping Families Dealing with Illness

The Harbor of Mercy is an organization that accompanies families dealing with severe illnesses of a family member. A team of rabbis and doctors provide support and real-time responses to these families.
The site theme is medicine and law, but the target market is religious Jewish families in crisis. Thus, the site design needs to combine:
- professional, conservative, serious
- spiritual
- warm hug

Target Market(s)

religious families suffering a health crisis

Industry/Entity Type

Non-profit organization

Number of Pages Required

1 page

Font styles to use
Sans Serif

Requirements
Must have
• Final design in PSD format. List of fonts used, colors used and link/button colors used in the design.

```html
<!DOCTYPE html>
<html lang="en">
<head>
<meta charset="utf-8">
<title>Harbor of Mercy</title>
<link href="https://fonts.googleapis.com/css2?family=Poppins:wght@400;500;600;700&family=Open+Sans:wght@400;600;700&display=swap" rel="stylesheet">
<style>
:root{
  --teal:#17a6a7;
  --teal-dark:#0e8586;
  --teal-light:#e4f3f3;
  --orange:#f0962b;
  --ink:#1f2a2e;
  --text:#5d6668;
  --line:#d8dfe0;
  --white:#ffffff;
  --paper:#f6f8f8;
}
*{margin:0;padding:0;box-sizing:border-box}
html,body{width:1200px;height:4680px;overflow:hidden}
body{font-family:"Open Sans",sans-serif;color:var(--text);background:var(--white);position:relative}
h1,h2,h3,h4{font-family:"Poppins",sans-serif;color:var(--ink);font-weight:600}
.abs{position:absolute}
.photo{position:absolute}
.btn{display:inline-block;background:var(--orange);color:var(--white);font-family:"Poppins",sans-serif;font-weight:600;font-size:13px;text-transform:uppercase;padding:12px 26px;border-radius:4px;letter-spacing:.5px}

/* top bar */
.topbar{position:absolute;left:0;top:0;width:1200px;height:32px;background:var(--teal);display:flex;align-items:center;padding-left:140px;gap:34px}
.topbar span{color:var(--white);font-size:13px;font-weight:600;display:flex;align-items:center;gap:6px}
.topbar i{width:8px;height:8px;border-radius:50%;background:var(--white);display:inline-block}
.nav{position:absolute;left:0;top:32px;width:1200px;height:80px;background:var(--white);display:flex;align-items:center;padding-left:130px;gap:44px;font-family:"Poppins",sans-serif;font-size:15px;color:var(--ink)}
.nav .active{color:var(--teal);border-bottom:3px solid var(--teal);padding-bottom:6px}
.brand{position:absolute;right:60px;top:0;height:112px;display:flex;align-items:center;gap:10px;background:var(--white);padding:0 18px;font-family:"Poppins",sans-serif;font-weight:700;font-size:22px;color:var(--teal)}
.brand b{width:16px;height:16px;background:var(--orange);border-radius:50%}

/* hero */
.hero{position:absolute;left:0;top:112px;width:1200px;height:600px;background:var(--paper);overflow:hidden}
.hero .photo{left:180px;top:0;width:1020px;height:600px;background:linear-gradient(120deg,#e9eeee 0%,#d7e6e8 45%,#c4d6da 70%,#e8e2da 100%)}
.hero-circle{position:absolute;left:70px;top:60px;width:420px;height:420px;border-radius:50%;background:var(--white);border:10px solid rgba(23,166,167,.25);box-shadow:0 0 0 3px var(--teal);display:flex;flex-direction:column;align-items:center;justify-content:center;text-align:center}
.hero-circle h1{font-size:40px;line-height:1.3;font-weight:600}
.hero-circle mark{background:var(--orange);color:var(--white);padding:0 8px;border-radius:4px}
.hero-rule{left:0;top:712px;width:1200px;height:8px;background:var(--teal)}
.hero-rule2{left:0;top:720px;width:1200px;height:5px;background:var(--orange)}

/* about */
.about-block{left:80px;top:840px;width:320px;height:320px;background:var(--teal)}
.about-photo{left:100px;top:860px;width:380px;height:260px;background:linear-gradient(135deg,#dfe8ea,#b9ccd0)}
.play{position:absolute;left:250px;top:950px;width:60px;height:60px;border-radius:50%;background:rgba(255,255,255,.9);display:flex;align-items:center;justify-content:center}
.play-label{left:222px;top:1018px;color:var(--white);font-family:"Poppins",sans-serif;font-size:12px;font-weight:600;letter-spacing:1px}
.about-copy{left:632px;top:850px;width:480px}
.section-title{font-size:34px;text-transform:uppercase;font-weight:500;display:flex;align-items:center}
.about-copy p{font-size:14px;line-height:1.7;margin-top:14px}

/* moral issues */
.moral-photo{left:432px;top:1320px;width:676px;height:360px;background:linear-gradient(120deg,#eef1f1,#cfdde0 60%,#b7cbd0)}
.moral-accent{left:100px;top:1580px;width:90px;height:140px;background:var(--orange)}
.moral-card{left:112px;top:1380px;width:480px;height:300px;background:var(--white);box-shadow:0 6px 24px rgba(0,0,0,.12);padding:34px 40px;text-align:center;border-top:4px solid var(--teal)}
.moral-card h2{font-size:26px;text-transform:uppercase;font-weight:500}
.moral-card .lead{color:var(--ink);font-weight:700;font-size:14px;margin-top:16px;line-height:1.5}
.moral-card p{font-size:13px;line-height:1.7;margin-top:14px}
.dots{left:300px;top:1664px;display:flex;gap:10px}
.dots i{width:8px;height:8px;border-radius:50%;background:var(--line)}
.dots i:first-child{background:var(--teal)}

/* services */
.service{position:absolute;top:1872px;width:228px;height:356px;background:var(--white);box-shadow:0 4px 16px rgba(0,0,0,.1);text-align:center}
.service .photo{position:relative;width:228px;height:170px;background:linear-gradient(135deg,#d9e3e5,#aebfc4)}
.service .icon{width:54px;height:54px;border-radius:50%;background:var(--white);border:3px solid var(--teal);margin:-27px auto 0;position:relative}
.service h3{color:var(--teal);font-size:17px;text-transform:uppercase;margin-top:8px}
.service p{font-size:11px;line-height:1.6;padding:6px 18px 0}
.service .btn{font-size:10px;padding:7px 16px;margin-top:12px}

/* testimonials */
.testi-band{left:0;top:2300px;width:1200px;height:520px;background:var(--teal-light);border-top:6px solid var(--teal)}
.testimonials-title{left:0;top:2356px;width:1200px;justify-content:center;font-size:32px}
.testi{position:absolute;top:2448px;width:440px;height:260px;background:var(--white);box-shadow:0 4px 16px rgba(0,0,0,.1);padding:32px 36px}
.testi .who{display:flex;align-items:center;gap:14px}
.testi .avatar{width:56px;height:56px;border-radius:50%;background:linear-gradient(135deg,#c9b9a9,#9d8a78)}
.testi h4{font-size:16px}
.stars{color:var(--orange);font-size:14px;letter-spacing:2px}
.quote{position:absolute;right:34px;top:28px;font-family:"Poppins",sans-serif;font-size:72px;line-height:1;color:var(--teal);font-weight:700}
.testi p{font-size:13px;line-height:1.7;margin-top:18px}
.arrow{position:absolute;top:2560px}

/* news */
.news-title{left:120px;top:2830px;font-size:32px}
.news{position:absolute;top:2920px;width:310px;height:300px}
.news .photo{position:relative;width:310px;height:180px;background:linear-gradient(135deg,#e0e8ea,#aec1c6)}
.news .body{position:relative;margin:-30px 24px 0;background:var(--white);box-shadow:0 4px 16px rgba(0,0,0,.12);padding:30px 20px 18px;text-align:center;min-height:150px}
.news .date{position:absolute;left:50%;top:-14px;transform:translateX(-50%);background:var(--orange);color:var(--white);font-size:11px;font-weight:600;padding:5px 16px;border-radius:3px;white-space:nowrap}
.news h4{font-size:15px;line-height:1.35}
.news p{font-size:11px;line-height:1.6;margin-top:8px}
.news .more{display:block;margin-top:10px;font-family:"Poppins",sans-serif;font-size:11px;font-weight:600;color:var(--ink);text-transform:uppercase}

/* ask the rabbi */
.ask-bg{left:0;top:3320px;width:1200px;height:460px;background:var(--paper)}
.ask-photo{left:140px;top:3320px;width:440px;height:460px;background:linear-gradient(160deg,#e3e9ea,#b7c8cc 55%,#8aa3aa)}
.ask-title{left:612px;top:3384px;font-size:32px}
.form{position:absolute;left:612px;top:3464px;width:448px;display:grid;grid-template-columns:1fr 1fr;gap:12px 20px}
.field{height:38px;border:1px solid var(--line);background:var(--white);font-size:12px;color:var(--text);padding:10px 12px}
.field.wide{grid-column:1/3}
.field.msg{grid-column:1/3;height:92px}
.form .send{grid-column:1/2;justify-self:start;background:var(--teal);color:var(--white);font-family:"Poppins",sans-serif;font-weight:600;font-size:13px;padding:12px 26px;text-transform:uppercase;border-radius:3px}

/* subscribe */
.sub-title{left:0;top:3960px;width:1200px;justify-content:center;font-size:32px}
.sub-note{left:0;top:4030px;width:1200px;text-align:center;font-size:15px}
.sub-form{left:300px;top:4074px;width:588px;height:56px;border:1px solid var(--line);display:flex;align-items:center;background:var(--white)}
.sub-form .mail{flex:1;padding-left:20px;font-size:14px;display:flex;align-items:center;gap:10px}
.sub-form .go{height:56px;background:var(--orange);color:var(--white);font-family:"Poppins",sans-serif;font-weight:600;font-size:14px;padding:0 30px;display:flex;align-items:center;text-transform:uppercase}

/* footer */
.footer-bg{left:0;top:4160px;width:1200px;height:460px;background:var(--teal);border-top:6px solid var(--orange)}
.footer-circle{left:80px;top:4196px;width:360px;height:360px;border-radius:50%;background:rgba(255,255,255,.14);display:flex;flex-direction:column;align-items:center;justify-content:center;gap:22px}
.footer-brand{font-family:"Poppins",sans-serif;font-weight:700;font-size:30px;color:var(--white);display:flex;align-items:center;gap:10px}
.footer-brand b{width:18px;height:18px;border-radius:50%;background:var(--white)}
.socials{display:flex;gap:14px}
.socials i{width:34px;height:34px;border-radius:50%;background:var(--white);opacity:.9}
.footer-col{position:absolute;top:4236px;color:var(--white)}
.footer-col h4{color:var(--white);font-size:18px;margin-bottom:6px}
.footer-col .rule{width:40px;height:3px;background:var(--orange);margin-bottom:14px}
.footer-col ul{list-style:none;font-size:13px;line-height:2}
.contact-row{display:flex;gap:10px;align-items:flex-start;font-size:13px;line-height:1.5;margin-bottom:16px}
.contact-row i{width:28px;height:28px;border-radius:50%;background:var(--orange);flex:none}
.copyright{left:0;top:4620px;width:1200px;height:60px;background:var(--teal-dark);color:var(--white);font-size:12px;display:flex;align-items:center;justify-content:center}
</style>
</head>
<body>

<header>
  <div class="topbar">
    <span><i></i>Search</span><span><i></i>Social</span><span><i></i>Contact</span><span><i></i>Hotline</span><span><i></i>Dedication II</span><span><i></i>Dedication I</span>
  </div>
  <nav class="nav">
    <span class="active">Home</span><span>About Us</span><span>Courses</span><span>Conferences</span><span>News</span><span>Resources</span><span>Contact</span>
  </nav>
  <div class="brand"><b></b>Harbor of Mercy</div>
</header>

<section class="hero">
  <div class="photo" role="img" aria-label="Photo of a doctor smiling with a patient holding a tablet in a clinic"></div>
  <div class="hero-circle">
    <h1>Should <mark>Morphine</mark><br>be given to the<br>patient?</h1>
  </div>
</section>
<div class="abs hero-rule"></div>
<div class="abs hero-rule2"></div>

<section class="about">
  <div class="abs about-block"></div>
  <div class="photo about-photo" role="img" aria-label="Photo of a doctor speaking with an elderly patient"></div>
  <div class="play"><svg width="22" height="24" viewBox="0 0 22 24"><path d="M2 2 L20 12 L2 22Z" fill="var(--teal)"/></svg></div>
  <div class="abs play-label">PLAY VIDEO</div>
  <div class="abs about-copy">
    <h2 class="section-title">About Us</h2>
    <p>Lorem ipsum dolor sit amet, consectetur adipiscing elit, sed do eiusmod tempor incididunt ut labore et dolore magna aliqua. Quis ipsum suspendisse ultrices gravida. Risus commodo viverra maecenas accumsan lacus vel facilisis.</p>
    <p>Lorem ipsum dolor sit amet, consectetur adipiscing elit, sed do eiusmod tempor incididunt ut labore et.</p>
    <p><span class="btn">Learn More</span></p>
  </div>
</section>

<section class="moral">
  <div class="photo moral-photo" role="img" aria-label="Photo of a doctor showing a clipboard to a smiling patient"></div>
  <div class="abs moral-accent"></div>
  <div class="abs moral-card">
    <h2>More Moral Issues</h2>
    <p class="lead">Lorem ipsum dolor sit amet, consectetur adipiscing elit, sed do eiusmod tempor incididunt</p>
    <p>Ut labore et dolore magna aliqua. Quis ipsum suspendisse ultrices gravida. Risus commodo viverra maecenas accumsan lacus vel facilisis.</p>
  </div>
  <div class="abs dots"><i></i><i></i><i></i><i></i></div>
</section>

<section class="services">
  <div class="service" style="left:100px"><div class="photo" role="img" aria-label="Photo of people attending a course"></div><div class="icon"></div><h3>Courses</h3><p>Lorem ipsum dolor sit amet, consectetur adipiscing elit, sed do eiusmod tempor.</p><span class="btn">Learn More</span></div>
  <div class="service" style="left:352px"><div class="photo" role="img" aria-label="Photo of an audience at a conference"></div><div class="icon"></div><h3>Conferences</h3><p>Lorem ipsum dolor sit amet, consectetur adipiscing elit, sed do eiusmod tempor.</p><span class="btn">Learn More</span></div>
  <div class="service" style="left:604px"><div class="photo" role="img" aria-label="Photo of a speaker giving a lecture"></div><div class="icon"></div><h3>Lectures</h3><p>Lorem ipsum dolor sit amet, consectetur adipiscing elit, sed do eiusmod tempor.</p><span class="btn">Learn More</span></div>
  <div class="service" style="left:856px"><div class="photo" role="img" aria-label="Photo of a hotline operator with a headset"></div><div class="icon"></div><h3>Hotline 24/7</h3><p>Lorem ipsum dolor sit amet, consectetur adipiscing elit, sed do eiusmod tempor.</p><span class="btn">Learn More</span></div>
</section>

<section class="testimonials">
  <div class="abs testi-band"></div>
  <h2 class="abs section-title testimonials-title">Testimonials</h2>
  <svg class="arrow" style="left:92px" width="20" height="30" viewBox="0 0 20 30"><polyline points="16,2 4,15 16,28" fill="none" stroke="var(--teal)" stroke-width="4"/></svg>
  <svg class="arrow" style="left:1100px" width="20" height="30" viewBox="0 0 20 30"><polyline points="4,2 16,15 4,28" fill="none" stroke="var(--teal)" stroke-width="4"/></svg>
  <div class="testi" style="left:148px">
    <div class="who"><div class="avatar" role="img" aria-label="Portrait photo of the reviewer"></div><div><h4>Daniel Hartley</h4><div class="stars">★★★★★</div></div></div>
    <div class="quote">”</div>
    <p>Lorem ipsum dolor sit amet, consectetur adipiscing elit, sed do eiusmod tempor incididunt ut labore et dolore magna aliqua. Ut enim ad minim veniam, quis nostrud exercitation ullamco.</p>
  </div>
  <div class="testi" style="left:620px">
    <div class="who"><div class="avatar" role="img" aria-label="Portrait photo of the reviewer"></div><div><h4>Daniel Hartley</h4><div class="stars">★★★★★</div></div></div>
    <div class="quote">”</div>
    <p>Lorem ipsum dolor sit amet, consectetur adipiscing elit, sed do eiusmod tempor incididunt ut labore et dolore magna aliqua. Ut enim ad minim veniam, quis nostrud exercitation ullamco.</p>
  </div>
</section>

<section class="latest">
  <h2 class="abs section-title news-title">Latest News</h2>
  <article class="news" style="left:120px"><div class="photo" role="img" aria-label="Photo of a nurse caring for a patient in bed"></div><div class="body"><span class="date">May 20, 2023</span><h4>What are Rabe Narratives?</h4><p>Short notes for families on care, faith and hard choices.</p><span class="more">Learn More</span></div></article>
  <article class="news" style="left:446px"><div class="photo" role="img" aria-label="Photo of a doctor talking with a patient"></div><div class="body"><span class="date">May 20, 2023</span><h4>Breakup Etiquette for Nannies to their Families</h4><p>Short notes for families on care, faith and hard choices.</p><span class="more">Learn More</span></div></article>
  <article class="news" style="left:778px"><div class="photo" role="img" aria-label="Photo of medical staff with a patient"></div><div class="body"><span class="date">May 20, 2023</span><h4>Breakup Etiquette for Families to their Nanny</h4><p>Short notes for families on care, faith and hard choices.</p><span class="more">Learn More</span></div></article>
</section>

<section class="ask">
  <div class="abs ask-bg"></div>
  <div class="photo ask-photo" role="img" aria-label="Photo of a smiling man in a wheelchair with a nurse in a hospital corridor"></div>
  <h2 class="abs section-title ask-title">Ask the Rabbi</h2>
  <div class="form">
    <div class="field">First Name</div><div class="field">Last Name</div>
    <div class="field">Phone Number</div><div class="field">Email address</div>
    <div class="field wide">Subject</div>
    <div class="field msg">Message</div>
    <span class="send">Send Message</span>
  </div>
</section>

<section class="subscribe">
  <h2 class="abs section-title sub-title">Subscribe Newsletter</h2>
  <p class="abs sub-note">Please sign up your email &amp; get updates.</p>
  <div class="abs sub-form">
    <div class="mail"><svg width="20" height="14" viewBox="0 0 20 14"><rect x="1" y="1" width="18" height="12" fill="none" stroke="var(--orange)" stroke-width="2"/><polyline points="1,1 10,8 19,1" fill="none" stroke="var(--orange)" stroke-width="2"/></svg>E-mail address</div>
    <div class="go">Subscribe ➤</div>
  </div>
</section>

<footer>
  <div class="abs footer-bg"></div>
  <div class="abs footer-circle">
    <div class="footer-brand"><b></b>Harbor of Mercy</div>
    <div class="socials"><i></i><i></i><i></i></div>
  </div>
  <div class="footer-col" style="left:472px">
    <h4>Quick Links</h4><div class="rule"></div>
    <div style="display:flex;gap:60px">
      <ul><li>About</li><li>Our Services</li><li>Courses</li><li>Lectures</li><li>News</li></ul>
      <ul><li>Testimonials</li><li>Conference</li><li>Blog</li><li>Contact</li></ul>
    </div>
  </div>
  <div class="footer-col" style="left:800px">
    <h4>Contact Us</h4><div class="rule"></div>
    <div class="contact-row"><i></i><div>24/7 Hotline Service<br>(555) 014-2020</div></div>
    <div class="contact-row"><i></i><div>Email us at<br>info@harborofmercy.org</div></div>
  </div>
  <div class="abs copyright">© 2023 Harbor of Mercy All Rights Reserved</div>
</footer>

</body>
</html>
```